International Internship Provider Needs Catalogue Layout & Design

We need a catalogue/booklet created to send out to university students and study abroad offices. We provide international internships to university students and young professionals in a range of fields in nine cities across the globe. Our program includes guaranteed internship, accommodation, social events, and support from staff. We would like to provide a clean, glossy, and picture-heavy publication to promote our program and website. We'd like to use captivating colors and the final product should convey what our program does and express the fun of living abroad with the professionalism of an internship.

Reason: We've increased the budget by $100, and we understand the project is a large undertaking. Thank you!

We would like each location to be two pages with large images of that location as well as all of the copy in the word document attached. Attached on the images is as an example of another catalogue we liked the style of for you to look at it. If you need any more details or would like me to break up the copy into sections please do not hesitate to ask. thank you!  

I've added new file of content that includes everything in the previous file plus more information, but on separate pages to help make it clear what information goes together. The location should still be a two-page spread that includes a large location image. We would like to have a quote from a student on each of those pages as well. 

I've added more photos for the location pages labeled by the location (ex: London_girls). I've also added some photos for Project Kelvo and new content. Please contact me with any questions. 

Reason: We realized we've asked for a few more edits from designers and we appreciate the time it takes to be make these constant edits. Thank you!

University students and recent college graduates. Usually the target market is between 21-23 years of age, and most students who travel abroad are female.

University

• It must be at least 10 pages and use the logo I've attached. Please be sure to look at the word document that is full of content that will be used in the project. Large photos of the locations are ideal as well 2 pages for each location.
• I have loads of photos I can give to you to use in the document, but you can use placeholders for now or some of the photos I've attached. I've also included a document full of copy that will need to be in the document just to give you an idea of where things will be displayed.

```html
<!DOCTYPE html>
<html lang="en">
<head>
<meta charset="utf-8">
<title>Project Kelvo – New York City Spread</title>
<link href="https://fonts.googleapis.com/css2?family=Open+Sans:wght@400;600&family=Oswald:wght@400;500&family=Roboto+Condensed:ital,wght@0,400;0,700;1,400&family=Cinzel:wght@400&display=swap" rel="stylesheet">
<style>
  :root{
    --bg:#d9d9dc;
    --paper:#ffffff;
    --green:#1f9a3e;
    --lime:#8cc63f;
    --ink:#2d2d2d;
    --sky-top:#4fa3d8;
    --sky-mid:#b9d6e6;
    --dusk:#e9c9a4;
    --harbor:#3c6f94;
  }
  *{box-sizing:border-box;margin:0;padding:0}
  html,body{width:1200px;height:818px;overflow:hidden;background:var(--bg)}
  .spread{position:absolute;left:50px;top:40px;width:1100px;height:738px;display:flex;box-shadow:0 12px 30px rgba(0,0,0,.25)}
  .page{position:relative;width:550px;height:738px;overflow:hidden}
  .page--left{background:var(--paper)}
  .skyline-fade{position:absolute;left:0;right:250px;bottom:0;height:420px;
    background:linear-gradient(to bottom,rgba(255,255,255,1),rgba(200,215,228,.55) 45%,rgba(215,205,180,.5) 75%,rgba(255,255,255,.9))}
  .copy{position:absolute;left:30px;top:150px;width:270px;font-family:"Open Sans",sans-serif;color:var(--ink);font-size:13px;line-height:1.4}
  .copy h2{font-family:"Open Sans",sans-serif;font-weight:600;color:var(--green);font-size:16px;margin:16px 0 4px}
  .copy h2:first-child{margin-top:0}
  .copy ul{padding-left:18px}
  .photo-col{position:absolute;left:300px;top:0;width:250px}
  .photo{display:block;width:250px}
  .photo--garden{height:150px;background:linear-gradient(160deg,#6f8f5a,#c9c4b6 60%,#8a8a80)}
  .photo--theatre{height:120px;background:linear-gradient(180deg,#b12a2a,#e0b070 55%,#6b4a3a)}
  .photo--statue{height:180px;background:linear-gradient(180deg,#7fb6de,#cfe3ee 60%,#6f9a5a)}
  .quote{height:230px;background:var(--lime);color:#fff;padding:20px 20px;font-family:"Roboto Condensed",sans-serif;font-size:14px;line-height:1.4}
  .quote__mark{font-weight:700;font-size:20px;line-height:0}
  .quote__by{margin-top:8px;color:var(--ink);font-size:12px}
  .quote__by strong{font-weight:700}
  .folio{position:absolute;bottom:22px;display:flex;align-items:center;font-family:"Cinzel",serif;font-size:11px;color:var(--ink);letter-spacing:.5px;white-space:nowrap}
  .folio--left{left:0}
  .folio--right{right:0}
  .folio__num{background:var(--lime);color:#fff;font-family:"Open Sans",sans-serif;font-size:10px;padding:2px 8px;margin:0 6px}
  .folio--left .folio__num{padding-left:30px}
  .folio--right .folio__num{padding-right:30px}
  .page--right .hero{position:absolute;inset:0;
    background:linear-gradient(180deg,var(--sky-top) 0%,var(--sky-mid) 40%,var(--dusk) 62%,#9a9aa0 72%,var(--harbor) 85%,#2f5574 100%)}
  .statue-zone{position:absolute;left:130px;top:30px;width:420px;height:600px;
    background:radial-gradient(ellipse at 55% 50%,rgba(96,168,150,.9),rgba(96,168,150,.6) 55%,rgba(96,168,150,0) 75%)}
  .title{position:absolute;left:30px;top:50px;font-family:"Oswald",sans-serif;font-weight:400;font-size:42px;color:#fff;letter-spacing:.5px;white-space:nowrap}
  .page--right .folio{color:#fff}
</style>
</head>
<body>
<div class="spread">
  <section class="page page--left">
    <div class="skyline-fade" role="img" aria-label="Faded New York skyline across the harbor"></div>
    <div class="copy">
      <h2>Program Snapshot</h2>
      <p>Do you think it has what it takes the live and intern in the Big Apple? Challenge yourself with an 8 or 12 week internship in New York City and gain unparalleled experience in your career field.</p>
      <h2>Dates</h2>
      <ul><li>Spring and Fall 12 week programs</li><li>Summer 8 week program</li></ul>
      <h2>Inclusions</h2>
      <ul>
        <li>Guaranteed internship</li>
        <li>Centralized student-residence style housing</li>
        <li>Individualized career development and pre-departure support</li>
        <li>Support from local staff in New York City</li>
        <li>On-site orientation</li>
        <li>Medical/travel insurance</li>
      </ul>
      <h2>Shindigs &amp; Shenanigans</h2>
      <ul><li>Harbor Hawks baseball game</li><li>Broadway Musical</li><li>Canoeing on the Bronx River</li></ul>
    </div>
    <div class="photo-col">
      <div class="photo photo--garden" role="img" aria-label="Interns posing at a botanical garden entrance"></div>
      <div class="photo photo--theatre" role="img" aria-label="Interns in front of a Broadway theatre marquee"></div>
      <div class="photo photo--statue" role="img" aria-label="Two interns on Liberty Island with the statue behind"></div>
      <blockquote class="quote">
        <span class="quote__mark">“</span>I thought it was a very good experience for me. It was a resume booster and will help me land a full-time job. The program was really well organized and I think the pre-screen interview process to get into the program is great. All of the interns were like-minded: fun and hard workers.<span class="quote__mark">”</span>
        <p class="quote__by"><strong>Daniel,</strong> Lakeshore University</p>
      </blockquote>
    </div>
    <footer class="folio folio--left"><span class="folio__num">6</span>PROJECT KELVO</footer>
  </section>
  <section class="page page--right">
    <div class="hero" role="img" aria-label="Statue of Liberty against a blue sky with the Manhattan skyline at dusk"></div>
    <div class="statue-zone" role="img" aria-label="Statue of Liberty"></div>
    <h1 class="title">NEW YORK CITY, USA</h1>
    <footer class="folio folio--right">GO FURTHER ABROAD<span class="folio__num">15</span></footer>
  </section>
</div>
</body>
</html>
```